Bao Lotus Menu Design Project

This project is pretty straight forward. You will be given 3 files which include the following:
1. Our proposed menu
2. Our Company logo
3. A sample menu on what we are looking for design wise

Your job is to create a visually pleasing menu that is simple, clean and fresh. Please refer to our home website for additional information. (www.baolotus-example.com) Must be in eps or equivalent format.

Target Market(s)

20s to 40s

Industry/Entity Type

It Company

Requirements
Must have
• Company log
Must be in EPS format

```html
<!DOCTYPE html>
<html lang="en">
<head>
<meta charset="utf-8">
<title>Bao Lotus – Chicken Menu</title>
<link rel="stylesheet" href="https://fonts.googleapis.com/css2?family=EB+Garamond:wght@400;500&display=swap">
<style>
  :root {
    --canvas: #ffffff;
    --page-top: #2b2b2b;
    --page-bottom: #151515;
    --ink: #f2f2f2;
    --ink-soft: #d9d9d9;
    --accent: #ff2a0a;
    --line: 17.8px;
  }
  * { margin: 0; padding: 0; box-sizing: border-box; }
  html, body {
    width: 1200px; height: 900px; overflow: hidden;
    background: var(--canvas);
  }
  .menu-page {
    position: absolute; left: 311px; top: 60px;
    width: 559px; height: 767px;
    background: linear-gradient(180deg, var(--page-top) 0%, #222 45%, var(--page-bottom) 100%);
    font-family: "EB Garamond", Georgia, serif;
    color: var(--ink);
  }
  .brand {
    position: absolute; right: 40px; top: 44px;
    display: flex; align-items: center; gap: 7px;
  }
  .brand-mark { width: 12px; height: 12px; background: var(--accent); }
  .brand-name {
    font-size: 18px; font-weight: 500; color: var(--ink);
    letter-spacing: 0.5px;
  }
  .menu-list {
    position: absolute; left: 51px; top: 65px; width: 446px;
    list-style: none;
  }
  .menu-list li {
    height: var(--line); line-height: var(--line);
    display: flex; justify-content: space-between;
    white-space: nowrap;
  }
  .section-title { font-size: 14.5px; padding-left: 8px; letter-spacing: 0.4px; }
  .note, .item-desc { font-size: 9px; color: var(--ink-soft); }
  .item-name { font-size: 12px; font-weight: 500; padding-left: 8px; }
  .item-price { font-size: 9.5px; color: var(--ink-soft); }
  .accent-band {
    position: absolute; left: 0; right: 0; top: 704px; height: 23px;
    background: var(--accent);
  }
</style>
</head>
<body>
  <section class="menu-page">
    <div class="brand">
      <span class="brand-mark"></span>
      <span class="brand-name">Bao Lotus</span>
    </div>

    <ul class="menu-list">
      <li class="section-title">CHICKEN</li>
      <li class="note">For white meat chicken, add $1.00.</li>
      <li class="note">Enjoy a Half Chinese Chicken Salad or Plain Fried Rice with any entrée for $5.50</li>
      <li class="note">Can replace Chicken with Tofu for $1.50</li>
      <li></li>

      <li><span class="item-name">Orange Chicken</span><span class="item-price">11.95</span></li>
      <li class="item-desc">Crispy chicken breast with onions and red and green bell peppers in a tangy orange sauce.</li>

      <li><span class="item-name">General Tso's Chicken</span><span class="item-price">11.75</span></li>
      <li class="item-desc">Crispy dark meat chicken with chili peppers in a spicy</li>
      <li class="item-desc">tangerine sauce topped with scallions.</li>

      <li><span class="item-name">Kung Pao Chicken</span><span class="item-price">11.95</span></li>
      <li class="item-desc">Dark meat chicken with red bell peppers, peanuts, and water chestnuts in spicy red sauce.</li>

      <li><span class="item-name">Chicken Lettuce Cups</span><span class="item-price">11.75</span></li>
      <li class="item-desc">Minced white meat chicken with bell peppers, water chestnuts, black mushrooms, pine nuts, and white crunchies.</li>
      <li class="item-desc">Served with four lettuce cups.</li>

      <li><span class="item-name">Chicken With Asparagus</span><span class="item-price">11.95</span></li>
      <li class="item-desc">Chicken breast with asparagus and carrots in a lemon white wine sauce.</li>

      <li><span class="item-name">Chicken With Snow Peas</span><span class="item-price">11.75</span></li>
      <li class="item-desc">Chicken breast served with snow peas, fresh mushrooms, carrots, and sliced garlic.</li>

      <li><span class="item-name">Teriyaki Chicken Bowl</span><span class="item-price">11.95</span></li>
      <li class="item-desc">Dark meat chicken glazed in Teriyaki sauce placed over a bed of rice.</li>

      <li><span class="item-name">Tangerine Chicken</span><span class="item-price">11.75</span></li>
      <li class="item-desc">Crispy chicken breast topped with scallions in a tangerine sauce.</li>

      <li><span class="item-name">Almond Chicken</span><span class="item-price">11.95</span></li>
      <li class="item-desc">Dark meat chicken with bamboo shoots, celery, water chestnuts, and toasted almonds.</li>
      <li class="item-desc">Prepared regularly or mandarin-Style.</li>

      <li><span class="item-name">Lemon Chicken</span><span class="item-price">11.75</span></li>
      <li class="item-desc">Crispy chicken breast marinated in garlic and ginger; served with a tart lemon sauce on the side.</li>

      <li><span class="item-name">Cashew Chicken</span><span class="item-price">11.95</span></li>
      <li class="item-desc">Chicken breast, zucchini, onions, garlic, ginger, and cashews tossed in an oyster sauce.</li>

      <li><span class="item-name">Curry Chicken</span><span class="item-price">11.95</span></li>
      <li class="item-desc">Chicken breast with potatoes, onions, green peas, and carrots in a curry sauce.</li>

      <li><span class="item-name">Sweet And Sour Chicken</span><span class="item-price">11.50</span></li>
      <li class="item-desc">Crispy chicken breast, bell peppers, onions, and pineapple in a sweet and sour sauce.</li>
    </ul>

    <div class="accent-band"></div>
  </section>
</body>
</html>
```